New website design for small car detailing company.

We have a small cleaning company, our main focus is car detailing but we are also expanding to home and residential cleaning and power washing.
I would like the web site to have a simple layout and SEO friendly.
I would also like to have a contact page in which clients can contact us and upload pictures of the house or car so we can provide an estimate.
A Page that shows the services we offer.

Target Market(s)

High paying clients for car detailiing and focus on residential and commercial cleaning.

Industry/Entity Type

Cleaning Service

Coding

Coded - Design and coding required

Number of Pages Required

4 page

Font styles to use
Serif

Colors

Designer to choose only greyscale colors for use in the design.

Requirements
Must have
• A home page.
Blog page for SEO
Contact page with the choice of clients to upload theirs pictures so we can provide estimates with calendar integration so they can provide their available dates for service.
A pictures to sell our services.
Nice to have
• Simple but sleek desing, I am more interested in SEO Score than heavy loads

```html
<!DOCTYPE html>
<html lang="en">
<head>
<meta charset="utf-8">
<title>Harbor Line Mobile Detailing</title>
<link href="https://fonts.googleapis.com/css2?family=Playfair+Display:wght@500;600;700&family=Source+Serif+4:ital,wght@0,400;0,600;1,400&display=swap" rel="stylesheet">
<style>
:root{
  --accent:#111;
  --accent-soft:#ececec;
  --black:#000;
  --ink:#111;
  --text:#666;
  --muted:#888;
  --grey-bg:#f2f2f2;
  --panel:#2e2e2e;
  --line:#e2e2e2;
  --white:#fff;
  --head:'Playfair Display',serif;
  --body:'Source Serif 4',serif;
}
*{margin:0;padding:0;box-sizing:border-box}
html,body{width:1200px;height:4129px;overflow:hidden}
body{position:relative;background:var(--white);font-family:var(--body);color:var(--text)}
.abs{position:absolute}
.h{font-family:var(--head);color:var(--ink);font-weight:700;text-transform:uppercase;letter-spacing:.5px}
.kicker{font-size:13px;font-style:italic;color:var(--muted)}
.rule{width:50px;height:2px;background:var(--accent)}
.btn{display:flex;align-items:center;justify-content:center;font-family:var(--body);font-weight:600;font-size:13px;letter-spacing:.5px;color:var(--white);background:var(--accent);text-transform:uppercase}

/* top bar */
.topbar{left:0;top:0;width:1200px;height:34px;background:var(--black)}
.top-label{left:622px;top:9px;font-size:12px;color:#ddd}
.top-num{left:780px;top:7px;font-family:var(--body);font-weight:600;font-size:14px;color:var(--white)}
.top-btn{left:881px;top:0;width:157px;height:34px;font-size:12px;background:var(--white);color:var(--ink)}

/* header */
.brand{left:160px;top:44px;width:108px;height:118px;background:var(--white);border:3px solid var(--ink);border-radius:0 0 50px 50px;display:flex;flex-direction:column;align-items:center;justify-content:center;gap:6px;text-align:center;z-index:3}
.brand .dot{width:12px;height:12px;background:var(--ink)}
.brand span{font-family:var(--head);font-weight:700;font-size:11.5px;line-height:1.2;color:var(--ink)}
.nav-item{top:62px;font-size:13px;color:#333}
.nav-item.on{color:var(--ink);font-weight:600}
.nav-item.on::after{content:"";position:absolute;left:-6px;right:-6px;top:26px;height:2px;background:var(--accent)}
.search{left:830px;top:56px;width:208px;height:38px;border:1px solid #ccc;border-radius:20px;font-size:11px;color:#888;padding:11px 0 0 16px}

/* hero */
.hero{left:0;top:107px;width:1200px;height:604px;background:radial-gradient(circle at 72% 35%,#6a6a6a 0,#2a2a2a 35%,#0d0d0d 70%)}
.hero-circle{left:168px;top:252px;width:362px;height:362px;border-radius:50%;background:var(--white);display:flex;flex-direction:column;align-items:center;justify-content:center;text-align:center}
.hero-circle h1{font-family:var(--head);font-weight:700;font-size:29px;line-height:1.22;color:var(--ink);text-transform:uppercase}
.hero-circle .btn{margin-top:22px;width:168px;height:40px;font-size:12px}
.dots{left:620px;top:684px;display:flex;gap:6px}
.dots i{width:9px;height:9px;background:#777}
.dots i:first-child{background:var(--white)}

/* services */
.center{left:0;width:1200px;text-align:center}
.card{top:902px;width:248px;height:277px;background:var(--white);box-shadow:0 0 12px rgba(0,0,0,.1);padding:26px 12px 26px 18px}
.card.active{border-right:4px solid var(--accent)}
.card .ico{width:66px;height:58px}
.card h3{font-family:var(--body);font-weight:600;font-size:12.5px;color:var(--ink);text-transform:uppercase;white-space:nowrap;margin-top:30px}
.card p{font-size:11px;line-height:21px;margin-top:10px;padding-right:6px}
.card .more{font-size:11px;font-weight:600;color:var(--ink);margin-top:14px}

/* welcome */
.welcome-bg{left:0;top:1256px;width:825px;height:508px;background:var(--grey-bg)}
.welcome p{font-size:11px;line-height:19px}
.photo{background:linear-gradient(135deg,#8a8a8a,#c9c9c9 55%,#777)}
.callout{left:638px;top:1642px;width:202px;height:48px;background:var(--accent);display:flex;align-items:center;gap:14px;padding-left:12px}
.callout span{font-family:var(--body);font-weight:600;font-size:19px;color:var(--white);letter-spacing:1px}

/* car detailing */
.car{left:380px;top:1954px;width:440px;height:321px;background:radial-gradient(ellipse at 50% 50%,#d6d6d6 0,#a9a9a9 40%,rgba(255,255,255,0) 72%)}
.tag{background:var(--white);border:1px solid var(--line);box-shadow:0 1px 6px rgba(0,0,0,.12);font-family:var(--body);font-size:12px;color:var(--ink);padding:5px 12px;border-radius:3px}
.pin{width:10px;height:10px;border-radius:50%;background:var(--white);border:3px solid var(--ink)}

/* testimonial */
.testi{left:0;top:2502px;width:1200px;height:390px;background:var(--black)}
.avatar{left:216px;top:2694px;width:79px;height:79px;background:linear-gradient(160deg,#8c8c8c,#d0d0d0)}
.qmark{left:282px;top:2736px;width:26px;height:26px;background:var(--white)}
.faint{left:866px;top:2700px;width:230px;text-align:center;font-family:var(--head);font-weight:700;font-size:26px;line-height:1.2;color:#1a1a1a;text-transform:uppercase}

/* blog */
.post{top:3057px;width:257px}
.post .img{height:195px}
.post .date{margin-top:18px;display:inline-block;background:var(--accent);color:var(--white);font-family:var(--body);font-weight:600;font-size:11px;padding:3px 10px}
.post h4{font-family:var(--head);font-weight:600;font-size:14px;line-height:23px;color:var(--ink);margin-top:14px}

/* contact */
.contact-black{left:0;top:3585px;width:1200px;height:544px;background:var(--black)}
.contact-panel{left:0;top:3422px;width:713px;height:407px;background:linear-gradient(180deg,#3a3a3a,#2a2a2a)}
.field{height:39px;background:var(--white);font-size:10.5px;color:#888;padding:12px 0 0 13px}
.submit{left:162px;top:3715px;width:428px;height:37px;border:1px solid var(--white);color:var(--white);font-family:var(--body);font-weight:600;font-size:13px;display:flex;align-items:center;justify-content:center}

/* footer */
.foot h5{font-family:var(--head);font-weight:600;font-size:14px;color:var(--white)}
.foot ul{list-style:none;margin-top:22px}
.foot li{font-size:11px;color:#bbb;height:24px;position:relative;padding-left:16px}
.foot li::before{content:"";position:absolute;left:0;top:6px;width:4px;height:4px;background:#888;border-radius:50%}
.info{font-size:10.5px;color:#bbb;line-height:19px}
.big-brand{left:825px;top:3701px;width:213px;height:264px;border:4px solid var(--white);border-radius:0 0 100px 100px;display:flex;flex-direction:column;align-items:center;justify-content:center;gap:14px;text-align:center}
.big-brand i{width:22px;height:22px;background:var(--white)}
.big-brand span{font-family:var(--head);font-weight:700;font-size:22px;line-height:1.2;color:var(--white)}
.social{top:3987px;width:36px;height:36px;border-radius:50%;background:#4a4a4a}
.copy{left:0;top:4097px;width:1200px;text-align:center;font-size:11px;color:#ccc}
.copy b{font-weight:600;color:var(--white)}
</style>
</head>
<body>

<!-- top bar -->
<div class="abs topbar"></div>
<div class="abs top-label">Get Free Estimate :</div>
<svg class="abs" style="left:745px;top:6px" width="24" height="24" viewBox="0 0 24 24"><circle cx="12" cy="12" r="11" fill="none" stroke="#fff" stroke-width="1.5"/><path d="M8 7l2 0 1 3-1.5 1a6 6 0 0 0 3 3l1-1.5 3 1v2c-5 1-10-4-9-9z" fill="#fff"/></svg>
<div class="abs top-num">555 014 2290</div>
<div class="abs btn top-btn">Get Free Estimate</div>

<!-- header -->
<div class="abs brand"><div class="dot"></div><span>HARBOR LINE<br>MOBILE<br>DETAILING</span></div>
<nav>
<span class="abs nav-item on" style="left:486px">Home</span>
<span class="abs nav-item" style="left:546px">About Us</span>
<span class="abs nav-item" style="left:622px">Services</span>
<span class="abs nav-item" style="left:692px">Blog</span>
<span class="abs nav-item" style="left:742px">Contact Us</span>
</nav>
<div class="abs search">Search...</div>
<svg class="abs" style="left:1010px;top:67px" width="16" height="16" viewBox="0 0 16 16"><circle cx="6.5" cy="6.5" r="4.5" fill="none" stroke="#111" stroke-width="2"/><path d="M10 10l4 4" stroke="#111" stroke-width="2"/></svg>

<!-- hero -->
<div class="abs hero" role="img" aria-label="Detailer in gloves polishing a dark car in a studio"></div>
<div class="abs hero-circle"><h1>H.L.M Cleaning<br>Quality<br>Services for you</h1><div class="btn">Get Free Estimate</div></div>
<div class="abs dots"><i></i><i></i><i></i><i></i><i></i></div>

<!-- services -->
<div class="abs center kicker" style="top:786px">What We Do</div>
<h2 class="abs center h" style="top:810px;font-size:30px">Services We Provide</h2>
<div class="abs rule" style="left:575px;top:866px"></div>

<div class="abs card" style="left:205px">
  <svg class="ico" viewBox="0 0 66 58"><path d="M28 2h26l10 27-10 27H28z" fill="#ececec"/><g fill="none" stroke="#111" stroke-width="2"><path d="M6 40V30l5-10h20l5 10v10z"/><circle cx="13" cy="41" r="3"/><circle cx="29" cy="41" r="3"/><path d="M10 29h22"/></g></svg>
  <h3>Car Detailing</h3><p>Lorem Ipsum is simply dummy text of the printing and typesetting the Lorem Ipsum has been the.</p><div class="more">Read More ▸</div>
</div>
<div class="abs card active" style="left:476px">
  <svg class="ico" viewBox="0 0 66 58"><path d="M28 2h26l10 27-10 27H28z" fill="#ececec"/><g fill="none" stroke="#111" stroke-width="2"><path d="M16 44V22l12-10 12 10v22z"/><path d="M24 44V32h8v12"/><path d="M4 20h8v24H4z"/></g></svg>
  <h3>Home &amp; Residential Cleaning</h3><p>Lorem Ipsum is simply dummy text of the printing and typesetting the Lorem Ipsum has been the.</p><div class="more">Read More ▸</div>
</div>
<div class="abs card" style="left:747px">
  <svg class="ico" viewBox="0 0 66 58"><path d="M28 2h26l10 27-10 27H28z" fill="#ececec"/><g fill="none" stroke="#111" stroke-width="2"><rect x="12" y="22" width="18" height="24" rx="3"/><path d="M18 22v-8h6v8M24 14h10l4 4"/><path d="M30 36h8v10"/></g></svg>
  <h3>Power Washing</h3><p>Lorem Ipsum is simply dummy text of the printing and typesetting the Lorem Ipsum has been the.</p><div class="more">Read More ▸</div>
</div>

<!-- welcome -->
<div class="abs welcome-bg"></div>
<div class="abs welcome" style="left:162px;top:1339px;width:370px">
  <div class="kicker">Welcome To</div>
  <h2 class="h" style="font-size:28px;line-height:40px;margin-top:12px;width:420px">Harbor Line Mobile<br>Detailing</h2>
  <div class="rule" style="margin-top:12px;width:36px"></div>
  <p style="margin-top:24px">Lorem Ipsum is simply dummy text of the printing &amp; typeset ting industry. Lorem Ipsum has been the the industry's the standard dummy text ever since the this.</p>
  <p style="margin-top:12px">Lorem Ipsum is simply dummy text of the printing and took a typesetting industry. Lorem Ipsum has been the industry's the standard dummy text ever since the 1500s, when an unknown printer took a galley of type and scrambled</p>
</div>
<div class="abs btn" style="left:162px;top:1653px;width:122px;height:39px">Learn More</div>
<div class="abs photo" style="left:638px;top:1330px;width:562px;height:360px" role="img" aria-label="Worker in boots power washing a concrete path beside grass"></div>
<div class="abs callout"><svg width="24" height="24" viewBox="0 0 24 24"><path d="M5 3l4 0 2 5-2.5 2a11 11 0 0 0 5.5 5.5l2-2.5 5 2v4C12 21 3 12 5 3z" fill="#fff"/></svg><span>555 014 2290</span></div>

<!-- car detailing -->
<div class="abs center kicker" style="top:1832px">We Are Expert In</div>
<h2 class="abs center h" style="top:1856px;font-size:30px">Car Detailing</h2>
<div class="abs rule" style="left:575px;top:1912px"></div>
<div class="abs car" role="img" aria-label="Top view of a car surrounded by detailers cleaning it"></div>
<div class="abs tag" style="left:346px;top:2035px">Safety Materials</div>
<div class="abs pin" style="left:469px;top:2066px"></div>
<div class="abs tag" style="left:710px;top:2086px">Modern Equipment</div>
<div class="abs pin" style="left:685px;top:2110px"></div>
<div class="abs tag" style="left:293px;top:2155px">Contactless Washing</div>
<div class="abs pin" style="left:439px;top:2150px"></div>
<div class="abs pin" style="left:545px;top:2165px"></div>
<div class="abs tag" style="left:778px;top:2148px">Heightend Care</div>
<div class="abs pin" style="left:750px;top:2157px"></div>
<p class="abs center" style="top:2311px;font-size:11px;line-height:21px">Lorem Ipsum is simply dummy text of the printing and took a typesetting industry.<br>Lorem Ipsum has been the industry's the standard dummy text ever since the 1500s,<br>when an unknown printer took a galley of type and scrambled</p>
<div class="abs btn" style="left:516px;top:2387px;width:168px;height:40px">Get Free Estimate</div>

<!-- testimonials -->
<div class="abs testi"></div>
<div class="abs faint">Harbor Line<br>Mobile<br>Detailing</div>
<div class="abs" style="left:1005px;top:2630px;display:flex;gap:4px"><i style="width:8px;height:8px;background:#666"></i><i style="width:8px;height:8px;background:#fff"></i></div>
<div class="abs kicker" style="left:216px;top:2578px;color:#aaa">Testimonials</div>
<h2 class="abs h" style="left:214px;top:2598px;font-size:30px;color:#fff">Our Happy Customer</h2>
<div class="abs rule" style="left:216px;top:2645px;width:36px;background:#fff"></div>
<div class="abs avatar" role="img" aria-label="Portrait of a smiling client"></div>
<div class="abs qmark"></div>
<svg class="abs" style="left:287px;top:2742px" width="16" height="14" viewBox="0 0 16 14"><path d="M1 14V7l3-7h3L5 6h2v8zM9 14V7l3-7h3l-2 6h2v8z" fill="#111"/></svg>
<div class="abs" style="left:216px;top:2788px;font-size:12px;color:#fff">Client Name</div>
<p class="abs" style="left:376px;top:2700px;width:590px;font-size:13px;line-height:26px;color:#ddd">" Lorem Ipsum is simply dummy text of the printing and took a typesetting industry. Lorem Ipsum has been the industry's the standard dummy text ever since the 1500s, when an unknown printer took a galley of type and scrambled "</p>
<div class="abs" style="left:376px;top:2797px;width:14px;height:2px;background:#aaa"></div>
<div class="abs" style="left:400px;top:2788px;font-size:12px;font-style:italic;color:#aaa">Client Name</div>

<!-- blog -->
<h2 class="abs center h" style="top:2962px;font-size:30px">Blog Post</h2>
<div class="abs rule" style="left:575px;top:3016px"></div>
<article class="abs post" style="left:184px"><div class="img" style="background:linear-gradient(135deg,#444,#a0a0a0)" role="img" aria-label="Man power washing a car"></div><span class="date">31 Aug</span><h4>Lorem Ipsum is simply dummy text of the printing type Text.</h4></article>
<article class="abs post" style="left:471px"><div class="img" style="background:linear-gradient(135deg,#8c8c8c,#e6e6e6)" role="img" aria-label="Car covered in white foam"></div><span class="date">31 Aug</span><h4>Lorem Ipsum is simply dummy text of the printing type Text.</h4></article>
<article class="abs post" style="left:758px"><div class="img" style="background:linear-gradient(135deg,#d4d4d4,#f4f4f4 60%,#bdbdbd)" role="img" aria-label="Cleaners wiping a kitchen table"></div><span class="date">31 Aug</span><h4>Lorem Ipsum is simply dummy text of the printing type Text.</h4></article>

<!-- contact -->
<div class="abs contact-black"></div>
<div class="abs contact-panel" role="img" aria-label="Grey tinted house exterior"></div>
<h2 class="abs h" style="left:162px;top:3486px;font-size:30px;color:#fff">Contact Us</h2>
<div class="abs rule" style="left:162px;top:3533px;width:36px;background:#fff"></div>
<form>
<div class="abs field" style="left:162px;top:3569px;width:208px">Email *</div>
<div class="abs field" style="left:381px;top:3569px;width:209px">Preferred Dates *</div>
<svg class="abs" style="left:566px;top:3581px" width="14" height="14" viewBox="0 0 14 14"><rect x="1" y="2.5" width="12" height="10.5" fill="none" stroke="#666" stroke-width="1.2"/><path d="M1 5.5h12M4 1v3M10 1v3" stroke="#666" stroke-width="1.2"/></svg>
<div class="abs field" style="left:162px;top:3619px;width:208px">Phone*</div>
<div class="abs field" style="left:381px;top:3619px;width:209px">Services *</div>
<div class="abs field" style="left:162px;top:3667px;width:208px">Upload Pictures *</div>
<svg class="abs" style="left:348px;top:3679px" width="14" height="14" viewBox="0 0 14 14"><path d="M9 4L4 9a1.5 1.5 0 0 0 2 2l6-6a3 3 0 0 0-4-4L2 7a4 4 0 0 0 6 6" fill="none" stroke="#666" stroke-width="1.2"/></svg>
<div class="abs field" style="left:381px;top:3667px;width:209px">Message*</div>
<div class="abs submit">SUBMIT</div>
</form>

<!-- footer -->
<div class="abs big-brand"><i></i><span>HARBOR LINE<br>MOBILE<br>DETAILING</span></div>
<div class="abs social" style="left:868px" aria-label="Social profile"></div>
<div class="abs social" style="left:908px" aria-label="Social profile"></div>
<div class="abs social" style="left:948px" aria-label="Social profile"></div>

<div class="abs foot" style="left:162px;top:3871px"><h5>SITEMAP</h5><ul><li>Home</li><li>About</li><li>Services</li><li>Blog</li><li>Contact</li></ul></div>
<div class="abs foot" style="left:335px;top:3871px"><h5>SERVICES</h5><ul><li>Car Detailing</li><li>Home &amp; Residential Cleaning</li><li>Power Washing</li></ul></div>
<div class="abs foot" style="left:575px;top:3871px"><h5>CONTACT INFO</h5></div>
<svg class="abs" style="left:575px;top:3914px" width="14" height="18" viewBox="0 0 14 18"><path d="M7 1a6 6 0 0 1 6 6c0 4-6 10-6 10S1 11 1 7a6 6 0 0 1 6-6z" fill="none" stroke="#bbb" stroke-width="1.5"/><circle cx="7" cy="7" r="2" fill="#bbb"/></svg>
<div class="abs info" style="left:606px;top:3909px">HARBOR LINE MOBILE<br>1010 – Lorem ipsum simple<br>text print type text.</div>
<svg class="abs" style="left:575px;top:3985px" width="14" height="14" viewBox="0 0 24 24"><path d="M5 3l4 0 2 5-2.5 2a11 11 0 0 0 5.5 5.5l2-2.5 5 2v4C12 21 3 12 5 3z" fill="#bbb"/></svg>
<div class="abs info" style="left:606px;top:3983px">555 014 2290</div>
<svg class="abs" style="left:575px;top:4021px" width="16" height="12" viewBox="0 0 16 12"><rect width="16" height="12" fill="#bbb"/><path d="M0 0l8 6 8-6" fill="none" stroke="#000" stroke-width="1.2"/></svg>
<div class="abs info" style="left:606px;top:4017px">info@harborlinedetail.com</div>
<div class="abs" style="left:162px;top:4069px;width:876px;height:1px;background:#333"></div>
<div class="abs copy">©<b>Harbor Line Mobile Detailing</b> -2020 All rights reserved.</div>

</body>
</html>
```